Brill Insurance Agency - Business Cards

Hello, I am needing new trendy business cards for our Insurance Agency now that I have a new Logo. I have attached our new logo with several color options along with a business card design that I like. I am leaning towards burgundy and blue colors. I have attached our current business card. I have also attached a headshot of our company president, Martin Vale, that you can use if you wish. Thank you so much in advance for all the wonderful designs!!!!

Target Market(s)

We want to look very professional to potential customers and we also want to look very professional so insurance companies will want to contract with us to sell their product.

Industry/Entity Type

Insurance

Contact Information for Business Card

Martin Vale
mvale@brillagency.com
Business: 555-213-4087
Fax: 555-213-7751
Cell: 555-390-2618
Toll Free: 888-555-0194
42 W Elm Rd Carver, KS 66950
www.brillagency.net

Font styles to use
Serif
Sans Serif

Colors
0355a3
3277b5
f04a50
ec1f27

Requirements
Nice to have
• I love creativity. The more creative and balanced a business card design the more I will like it. I would like the card to be printed horizontally instead of vertically.
Should not have
• My project should not have the Allied Coverage Network logo. It is no longer used in the industry.

```html
<!DOCTYPE html>
<html lang="en">
<head>
<meta charset="utf-8">
<title>Brill Insurance Agency – Business Cards</title>
<link href="https://fonts.googleapis.com/css2?family=Mulish:wght@400;500;700&display=swap" rel="stylesheet">
<style>
  :root {
    --brand-blue: #1e5686;
    --ink: #3f3f3f;
    --muted: #9a9a9a;
    --paper: #ffffff;
    --backdrop: #f1f2f4;
  }
  * { margin: 0; padding: 0; box-sizing: border-box; }
  html, body { width: 1200px; height: 1000px; overflow: hidden; }
  body {
    background: var(--backdrop);
    font-family: "Mulish", Arial, sans-serif;
    position: relative;
  }
  .card { position: absolute; }

  /* Front */
  .card-front {
    left: 261px; top: 91px; width: 677px; height: 386px;
    background: var(--brand-blue);
    color: var(--paper);
    text-align: center;
  }
  .front-mark {
    position: absolute; left: 50%; top: 98px;
    width: 100px; height: 100px; margin-left: -50px;
    border: 9px solid var(--paper); border-radius: 50%;
  }
  .front-name {
    position: absolute; left: 0; right: 0; top: 218px;
    font-size: 34px; font-weight: 700; letter-spacing: 0.5px;
    text-transform: uppercase;
  }
  .front-web {
    position: absolute; left: 0; right: 0; top: 327px;
    font-size: 17px; font-weight: 500;
  }

  /* Back */
  .card-back {
    left: 260px; top: 519px; width: 680px; height: 388px;
    background: var(--paper);
    border: 1px solid #e4e4e4;
  }
  .back-brand {
    position: absolute; right: 40px; top: 53px;
    display: flex; align-items: center; gap: 12px;
  }
  .back-mark {
    width: 50px; height: 50px; border-radius: 50%;
    border: 6px solid var(--brand-blue);
  }
  .back-brand-name {
    font-size: 17px; font-weight: 700; color: var(--brand-blue);
    text-transform: uppercase; letter-spacing: 0.3px; white-space: nowrap;
  }
  .back-rule {
    position: absolute; left: 273px; top: 136px; width: 365px;
    border-top: 1.5px solid var(--brand-blue);
  }
  .accent-bar {
    position: absolute; left: 0; top: 113px; width: 10px; height: 110px;
    background: var(--brand-blue); border-radius: 0 4px 4px 0;
  }
  .person { position: absolute; left: 35px; top: 118px; }
  .person-first {
    font-size: 42px; font-weight: 400; color: var(--brand-blue);
    line-height: 42px; text-transform: uppercase;
  }
  .person-last {
    font-size: 40px; font-weight: 400; color: var(--ink); line-height: 36px;
  }
  .person-title { font-size: 16px; color: var(--muted); margin-top: 6px; }

  .contact {
    position: absolute; right: 90px; text-align: right;
    font-size: 17px; color: var(--ink); line-height: 21px; white-space: nowrap;
  }
  .contact .label { color: var(--muted); }
  .contact-phones { top: 159px; }
  .contact-fax { top: 221px; }
  .contact-web { top: 262px; }
  .contact-address { top: 322px; }

  .icon-rail {
    position: absolute; left: 605px; top: 158px; width: 34px; height: 147px;
    background: var(--brand-blue); border-radius: 4px;
  }
  .icon-rail svg { position: absolute; left: 7px; width: 20px; height: 20px; }
  .pin { position: absolute; left: 612px; top: 326px; width: 18px; height: 22px; }

  .toll-free {
    position: absolute; left: 35px; top: 344px;
    font-size: 17px; color: var(--ink);
  }
  .toll-free .label { color: var(--muted); }
</style>
</head>
<body>

  <section class="card card-front">
    <div class="front-mark"></div>
    <div class="front-name">Brill Insurance Agency</div>
    <div class="front-web">www.brillagency.net</div>
  </section>

  <section class="card card-back">
    <div class="back-brand">
      <div class="back-mark"></div>
      <div class="back-brand-name">Brill Insurance Agency</div>
    </div>
    <div class="back-rule"></div>

    <div class="accent-bar"></div>
    <div class="person">
      <div class="person-first">Martin</div>
      <div class="person-last">Vale</div>
      <div class="person-title">Owner | CEO</div>
    </div>

    <div class="contact contact-phones">
      555 - 213 - 4087 <span class="label">(Business)</span><br>
      555 - 390 - 2618 <span class="label">(Cell)</span>
    </div>
    <div class="contact contact-fax">555 - 213 - 7751</div>
    <div class="contact contact-web">
      mvale@brillagency.com<br>www.brillagency.net
    </div>
    <div class="contact contact-address">
      42 W Elm Rd Carver<br>KS 66950
    </div>

    <div class="icon-rail">
      <svg style="top:12px" viewBox="0 0 24 24" aria-hidden="true">
        <path fill="#fff" d="M6.6 10.8a15.1 15.1 0 0 0 6.6 6.6l2.2-2.2a1 1 0 0 1 1-.25 11.4 11.4 0 0 0 3.6.57 1 1 0 0 1 1 1V20a1 1 0 0 1-1 1A17 17 0 0 1 3 4a1 1 0 0 1 1-1h3.5a1 1 0 0 1 1 1c0 1.25.2 2.45.57 3.57a1 1 0 0 1-.25 1z"/>
      </svg>
      <svg style="top:62px" viewBox="0 0 24 24" aria-hidden="true">
        <path fill="#fff" d="M3 8h3v13H3zM7 6h2V3h9v5h3v13H7zm4-1v3h5V5zm0 6v2h2v-2zm4 0v2h2v-2zm-4 4v2h2v-2zm4 0v2h2v-2z"/>
      </svg>
      <svg style="top:113px" viewBox="0 0 24 24" aria-hidden="true">
        <circle cx="12" cy="12" r="10" fill="#fff"/>
        <path fill="#1e5686" d="M6 7c2 0 3 1 3 2.5S7.5 12 8 13.5 10 15 10 17l-1 3a8 8 0 0 1-5-8c0-2 1-4 2-5zm8-3c1 1 1 2 3 2s2 2 1 3-3 0-3 2 2 2 3 4l-1 3a8 8 0 0 0 1-14z"/>
      </svg>
    </div>
    <svg class="pin" viewBox="0 0 24 30" aria-hidden="true">
      <path fill="#1e5686" d="M12 0a10 10 0 0 0-10 10c0 7.5 10 20 10 20s10-12.5 10-20A10 10 0 0 0 12 0zm0 14a4 4 0 1 1 0-8 4 4 0 0 1 0 8z"/>
    </svg>

    <div class="toll-free"><span class="label">Toll Free :</span> 888-555-0194</div>
  </section>

</body>
</html>
```